Flyer-Design für ambulanten Pflegedienst (Essen auf Rädern)
Zielgruppe
Wir betreiben einen ambulanten Pflegedienst. Die Flyer sollen in den Haushalten verteilt werden.
Aufgabenstellung
Für das Essen auf Rädern soll eine Flyer in einem originellen Format entworfen werden. Der Flyer könnte in einem runden Format sein und sollte hochwertig wirken. Vielleicht ein hochweriget Teller mit einem gesunden essen darauf. u
Folgender Text sollte enthalten sein:
Logo bitte der Homepage www.Kalveto.de entnehmen
Text auf dem neuen Flyer
Wenn Sie einen Pflegegrad haben, liefern wir Ihnen das Essen auf Rädern nach Hause

```html
<!DOCTYPE html>
<html lang="de">
<head>
<meta charset="utf-8">
<title>Kalveto – Essen auf Rädern Flyer</title>
<link rel="stylesheet" href="https://fonts.googleapis.com/css2?family=Open+Sans:ital,wght@0,400;0,600;1,400;1,700&display=swap">
<style>
  :root {
    --page: #fafaf7;
    --plate-dark: #262626;
    --panel-light: #e6e6e5;
    --ink: #1f1f1f;
    --ink-soft: #333333;
    --brand-green: #4b8a2c;
  }
  html, body {
    margin: 0;
    padding: 0;
    width: 1200px;
    height: 1200px;
    overflow: hidden;
    background: var(--page);
  }
  .canvas {
    position: relative;
    width: 1200px;
    height: 1200px;
  }
  .flyer {
    position: absolute;
    inset: 0;
    width: 1200px;
    height: 1200px;
    font-family: "Open Sans", Arial, sans-serif;
  }
  .rim-text {
    font-size: 12px;
    fill: var(--ink-soft);
    letter-spacing: 0.2px;
  }
  .brand-name {
    font-size: 40px;
    font-weight: 400;
    fill: var(--ink);
  }
  .brand-claim {
    font-size: 13px;
    font-weight: 600;
    fill: var(--ink);
  }
  .headline {
    font-size: 27px;
    font-style: italic;
    font-weight: 400;
    fill: var(--ink);
  }
  .headline .accent {
    font-weight: 700;
    fill: var(--brand-green);
  }
</style>
</head>
<body>
<div class="canvas">
  <svg class="flyer" viewBox="0 0 1200 1200" xmlns="http://www.w3.org/2000/svg">
    <defs>
      <clipPath id="flyer-disc">
        <circle cx="600" cy="600" r="360"/>
      </clipPath>
      <radialGradient id="salad-tones" cx="0.62" cy="0.5" r="0.6">
        <stop offset="0" stop-color="#5d6b2e"/>
        <stop offset="0.45" stop-color="#6b7d34"/>
        <stop offset="0.75" stop-color="#3e4a22"/>
        <stop offset="1" stop-color="#262626"/>
      </radialGradient>
      <radialGradient id="salad-faint" cx="0.2" cy="0.5" r="0.8">
        <stop offset="0" stop-color="#d9dcd2"/>
        <stop offset="0.6" stop-color="#e3e4df"/>
        <stop offset="1" stop-color="#e8e8e7"/>
      </radialGradient>
      <path id="rim-path" d="M792 874 A335 335 0 0 0 767.5 310"/>
    </defs>

    <g clip-path="url(#flyer-disc)">
      <rect class="plate-photo" x="240" y="240" width="360" height="720" fill="var(--plate-dark)"/>
      <rect x="240" y="240" width="360" height="720" fill="url(#salad-tones)"
            role="img" aria-label="Foto: gesunder Salat mit Karotten, Oliven, roten Zwiebeln und Feta auf einem dunklen Teller"/>
      <rect class="info-panel" x="600" y="240" width="360" height="720" fill="url(#salad-faint)"
            role="img" aria-label="Blass überlagerte Fortsetzung des Salatfotos"/>
    </g>

    <path class="rim-line" d="M631 261 A340 340 0 0 1 794 325" fill="none" stroke="var(--brand-green)" stroke-width="1.3"/>
    <path class="rim-line" d="M631 944 A340 340 0 0 0 797 884" fill="none" stroke="var(--brand-green)" stroke-width="1.3"/>

    <text class="rim-text">
      <textPath href="#rim-path">Kalveto Der mobile Pflegedienst GmbH  ·  Lindenweg 12  ·  18273 Gravenau  ·  www.Kalveto.de</textPath>
    </text>

    <g class="brand">
      <rect x="634" y="540" width="22" height="22" fill="var(--brand-green)"/>
      <text class="brand-name" x="668" y="564">Kalveto</text>
      <text class="brand-claim" x="668" y="588">Der Mobile Pflegedienst</text>
    </g>

    <text class="headline" x="632">
      <tspan x="632" y="672">Wenn Sie einen</tspan>
      <tspan x="632" y="709">Pflegegrad haben,</tspan>
      <tspan x="632" y="746">liefern wir Ihnen</tspan>
      <tspan x="632" y="783">das <tspan class="accent">Essen auf</tspan></tspan>
      <tspan x="632" y="820" class="accent">Rädern nach</tspan>
      <tspan x="632" y="857"><tspan class="accent">Hause</tspan>.</tspan>
    </text>
  </svg>
</div>
</body>
</html>
```